Disposable Mini Sauce Pot Design for Asian Chain Food Brands

We operate a Hainan Chicken Rice takeout brand under the name Wokly8, with our official website: www.Wokly8.com.
We offer four signature house sauces and are launching brand-new packaging for our sauce line. We require custom graphic designs exclusively for the sauce cup lids.
Product Material & Base Specs
The sauce cups are made of PP plastic, available in two translucent base options: Translucent White and Translucent Orange.
Four Sauce Varieties for Individual Lid Designs
1. Red Sauce – Fried Sweet Chili Sauce
2.Green Sauce – Scallion Oil Dressing
3.Sweet Soy Sauce
4.Sweet Red Sauce (Special for Fried Chicken)
Differentiate each sauce lid design through unique graphics, typography, or illustrative elements for easy customer identification.
The marking NET WT 2 OZ must be clearly printed on every lid.
**There is no need to print full descriptive text or the full name of the sauces on each lid; the design only needs to clearly differentiate the four sauce varieties.
**Please reference the original design style and brand color palette shown on our official website, and feel free to fully unleash your creativity.
Look and feel
Each slider illustrates characteristics of the customer's brand and the style your logo design should communicate.

```html
<!DOCTYPE html>
<html lang="en">
<head>
<meta charset="utf-8">
<title>Wokly8 Sauce Packaging Design</title>
<link href="https://fonts.googleapis.com/css2?family=Anton&family=Oswald:wght@500;600;700&family=Roboto+Condensed:wght@400;500;700&family=Cabin:wght@400;500&display=swap" rel="stylesheet">
<style>
  :root {
    --ink: #231F20;
    --black: #0e0e0e;
    --red: #C02629;
    --red-dark: #8f1b1d;
    --gold: #F7AB1B;
    --green-deep: #319345;
    --orange-red: #D74227;
    --tan: #DFB272;
    --lime: #81C041;
    --forest: #2c5f27;
    --cream: #fbf3e4;
    --white: #ffffff;
  }
  * { box-sizing: border-box; margin: 0; padding: 0; }
  html, body { width: 1200px; height: 962px; overflow: hidden; background: var(--white); }
  .canvas { position: relative; width: 1200px; height: 962px; overflow: hidden; background: var(--white); font-family: "Cabin", sans-serif; color: var(--ink); }

  .hero-band { position: absolute; left: 0; top: 0; width: 1200px; height: 515px; background: var(--black); }

  .hashtag { position: absolute; left: 857px; top: 16px; font-family: "Roboto Condensed", sans-serif; font-weight: 400; font-size: 24px; color: var(--white); letter-spacing: 0.3px; }

  .brand-mark { position: absolute; left: 45px; top: 44px; display: flex; align-items: center; gap: 12px; }
  .brand-mark .dot { width: 48px; height: 48px; border-radius: 50%; background: var(--red); }
  .brand-mark .name { font-family: "Anton", sans-serif; font-size: 46px; line-height: 1; color: var(--white); letter-spacing: 0.5px; }

  .page-title { position: absolute; left: 43px; top: 150px; font-family: "Roboto Condensed", sans-serif; font-weight: 700; font-size: 46px; line-height: 52px; color: var(--white); letter-spacing: 1px; }
  .tagline { position: absolute; left: 43px; top: 259px; font-family: "Cabin", sans-serif; font-size: 21px; color: var(--gold); }
  .intro { position: absolute; left: 41px; top: 309px; font-size: 21px; line-height: 27px; color: var(--white); }

  .values { position: absolute; left: 34px; top: 423px; display: flex; align-items: center; }
  .value { display: flex; align-items: center; gap: 10px; font-family: "Cabin", sans-serif; font-size: 13.5px; line-height: 16px; letter-spacing: 1.6px; color: var(--white); }
  .value svg { width: 26px; height: 40px; }
  .value-divider { width: 2px; height: 42px; background: var(--gold); margin: 0 12px; }

  .section-heading { position: absolute; left: 39px; font-family: "Roboto Condensed", sans-serif; font-weight: 700; font-size: 22px; letter-spacing: 3px; color: var(--ink); }
  .story-heading { top: 551px; }
  .story-text { position: absolute; left: 39px; top: 593px; width: 380px; font-size: 13.5px; line-height: 20.2px; letter-spacing: 1.5px; color: var(--ink); }
  .accent-rule { position: absolute; left: 39px; top: 733px; width: 64px; height: 4px; background: var(--red); }
  .palette-heading { top: 757px; }
  .swatches { position: absolute; left: 45px; top: 794px; display: flex; gap: 13px; }
  .swatch { width: 40px; text-align: center; }
  .swatch i { display: block; width: 40px; height: 40px; border-radius: 50%; }
  .swatch span { display: block; margin-top: 7px; font-size: 7.5px; letter-spacing: 0.2px; margin-left: -6px; margin-right: -6px; }

  /* Lid labels */
  .lid { position: absolute; width: 320px; height: 320px; border-radius: 34px; overflow: hidden; }
  .lid--red { left: 505px; top: 68px; background: var(--red); }
  .lid--sweet { left: 845px; top: 68px; background: var(--orange-red); }
  .lid--soy { left: 505px; top: 405px; background: var(--black); }
  .lid--green { left: 845px; top: 405px; background: var(--lime); }

  .lid-frame { position: absolute; inset: 11px; border: 3px solid; border-radius: 24px; overflow: hidden; }
  .lid--red .lid-frame { border-color: var(--gold); }
  .lid--sweet .lid-frame { border-color: var(--cream); }
  .lid--soy .lid-frame { border-color: var(--tan); }
  .lid--green .lid-frame { border-color: var(--forest); }

  .lid-brand { position: absolute; left: 32px; top: 36px; display: flex; align-items: center; gap: 7px; }
  .lid-brand .dot { width: 30px; height: 30px; border-radius: 50%; background: var(--cream); }
  .lid--red .lid-brand .dot, .lid--soy .lid-brand .dot { background: var(--gold); }
  .lid--green .lid-brand .dot { background: var(--forest); }
  .lid-brand .name { font-family: "Anton", sans-serif; font-size: 30px; line-height: 1; color: var(--white); }

  .lid-word { position: absolute; left: 30px; font-family: "Anton", sans-serif; line-height: 1; color: var(--cream); text-transform: uppercase; white-space: nowrap; z-index: 2; }
  .word-xl { font-size: 96px; letter-spacing: 1px; }
  .word-sauce { font-size: 44px; letter-spacing: 1px; }
  .word-kicker { font-size: 36px; letter-spacing: 6px; }

  .lid-art { position: absolute; border-radius: 40%; z-index: 1; }

  .lid-band { position: absolute; left: 18px; height: 27px; z-index: 3; clip-path: polygon(2% 8%, 100% 0, 97% 92%, 0 100%, 3% 50%); display: flex; align-items: center; justify-content: flex-start; font-family: "Oswald", sans-serif; font-weight: 700; font-size: 19px; letter-spacing: 0.5px; padding-left: 30px; white-space: nowrap; }
  .lid--red .lid-band { top: 230px; width: 200px; background: var(--black); color: var(--gold); font-style: italic; }
  .lid--sweet .lid-band { top: 232px; width: 238px; background: var(--black); color: var(--gold); padding-left: 20px; }
  .lid--soy .lid-band { top: 232px; width: 230px; background: var(--tan); color: var(--black); padding-left: 34px; }
  .lid--green .lid-band { top: 226px; width: 200px; background: var(--forest); color: #b8e27e; padding-left: 30px; }

  .lid-features { position: absolute; left: 36px; right: 34px; top: 265px; display: flex; align-items: center; font-family: "Oswald", sans-serif; font-weight: 500; font-size: 7.6px; line-height: 9.4px; letter-spacing: 0.4px; color: var(--white); }
  .feature { flex: 1; display: flex; align-items: center; gap: 5px; padding: 0 5px; white-space: nowrap; }
  .feature + .feature { border-left: 1.5px solid var(--gold); }
  .feature svg { width: 11px; height: 14px; flex: none; }
  .lid--sweet .feature + .feature { border-color: var(--cream); }
  .lid--soy .feature + .feature { border-color: var(--tan); }
  .lid--green .feature + .feature { border-color: var(--forest); }

  .lid-net { position: absolute; left: 14px; right: 14px; top: 290px; height: 17px; border-radius: 0 0 20px 20px; display: flex; align-items: center; justify-content: center; font-family: "Oswald", sans-serif; font-weight: 600; font-size: 9.5px; letter-spacing: 1.6px; }
  .lid--red .lid-net { background: var(--red-dark); color: var(--white); }
  .lid--sweet .lid-net { background: var(--cream); color: var(--orange-red); }
  .lid--soy .lid-net { background: var(--tan); color: var(--black); }
  .lid--green .lid-net { background: var(--forest); color: var(--white); }

  .review-note { position: absolute; left: 501px; top: 748px; width: 660px; font-size: 14.5px; line-height: 18px; letter-spacing: 1.5px; color: var(--ink); }
  .thanks { position: absolute; left: 501px; top: 818px; font-size: 14.5px; letter-spacing: 1.5px; }
  .tool-badges { position: absolute; left: 1081px; top: 803px; display: flex; gap: 9px; }
  .tool-badges i { width: 43px; height: 43px; border-radius: 6px; display: block; }
  .tool-badges .tool-a { background: #330000; }
  .tool-badges .tool-b { background: #001e36; }

  .footer-bar { position: absolute; left: 0; top: 881px; width: 1200px; height: 53px; background: var(--black); }
  .footer-frame { position: absolute; left: 6px; top: 887px; width: 1188px; height: 41px; border: 1.5px solid var(--orange-red); border-radius: 5px; }
  .footer-item { position: absolute; top: 896px; display: flex; align-items: center; gap: 18px; font-size: 15.5px; letter-spacing: 1.6px; color: var(--white); }
  .footer-item svg { width: 30px; height: 30px; }
  .footer-left { left: 80px; }
  .footer-right { left: 855px; }
  .footer-brand { position: absolute; left: 0; width: 1200px; top: 893px; text-align: center; font-family: "Anton", sans-serif; font-size: 24px; line-height: 30px; color: var(--white); }
</style>
</head>
<body>
<div class="canvas">
  <div class="hero-band"></div>
  <div class="hashtag">#Original Illustration Design</div>

  <div class="brand-mark"><span class="dot"></span><span class="name">Wokly8</span></div>

  <h1 class="page-title">SAUCE PACKAGING<br>DESIGN</h1>
  <p class="tagline">Bold Flavors. Fast Service. Always Wokly8.</p>
  <p class="intro">A vibrant, modern, and<br>flavor-driven sauce packaging<br>collection crafted to elevate</p>

  <div class="values">
    <div class="value">
      <svg viewBox="0 0 26 40"><path d="M13 3c2 7 10 11 10 22a10 10 0 0 1-20 0c0-5 3-8 5-11 0 4 2 6 3 6-1-6 0-12 2-17z" fill="none" stroke="#F7AB1B" stroke-width="2.4"/></svg>
      <span>BOLD<br>FLAVORS</span>
    </div>
    <span class="value-divider"></span>
    <div class="value">
      <svg viewBox="0 0 26 40"><path d="M20 5C8 9 3 18 5 30c10 0 17-9 15-25z" fill="none" stroke="#319345" stroke-width="2.2"/><path d="M7 38c3-10 7-18 11-26" fill="none" stroke="#319345" stroke-width="2"/></svg>
      <span>QUALITY<br>INGREDIENTS</span>
    </div>
    <span class="value-divider"></span>
    <div class="value">
      <svg viewBox="0 0 26 40"><path d="M13 4C9 13 3 19 3 26a10 10 0 0 0 20 0c0-7-6-13-10-22z" fill="none" stroke="#F7AB1B" stroke-width="2.2"/></svg>
      <span>MODERN<br>DESIGN</span>
    </div>
  </div>

  <h2 class="section-heading story-heading">DESIGN STORY</h2>
  <p class="story-text">This sauce collection is designed to stand out on shelves and in the hands of customers.<br>Each label uses a bold color that reflects the flavor profile and key ingredient, with fun illustrations and strong typography for instant recognition.</p>
  <div class="accent-rule"></div>
  <h2 class="section-heading palette-heading">COLOR PALETTE</h2>
  <div class="swatches">
    <div class="swatch"><i style="background:#000"></i><span>#231F20</span></div>
    <div class="swatch"><i style="background:var(--red)"></i><span>#C02629</span></div>
    <div class="swatch"><i style="background:var(--gold)"></i><span>#F7AB1B</span></div>
    <div class="swatch"><i style="background:var(--green-deep)"></i><span>#319345</span></div>
    <div class="swatch"><i style="background:var(--orange-red)"></i><span>#D74227</span></div>
    <div class="swatch"><i style="background:var(--tan)"></i><span>#DFB272</span></div>
    <div class="swatch"><i style="background:var(--lime)"></i><span>#81C041</span></div>
  </div>

  <!-- Red Sauce lid -->
  <div class="lid lid--red">
    <div class="lid-frame"></div>
    <div class="lid-brand"><span class="dot"></span><span class="name">Wokly8</span></div>
    <div class="lid-word word-xl" style="top:86px">RED</div>
    <div class="lid-word word-sauce" style="top:178px">SAUCE</div>
    <div class="lid-art" role="img" aria-label="Illustration of a red chili pepper with sauce splashes" style="left:200px;top:100px;width:98px;height:124px;background:linear-gradient(160deg,#3a8f2c 0%,#e02a2a 35%,#b01818 100%)"></div>
    <div class="lid-band">⸗ SWEET CHILI ⸗</div>
    <div class="lid-features">
      <div class="feature"><svg viewBox="0 0 11 14"><path d="M9 1C8 7 5 11 1 13c5 0 9-4 8-12z" fill="#F7AB1B"/></svg><span>MADE WITH<br>REAL CHILI</span></div>
      <div class="feature"><svg viewBox="0 0 11 14"><path d="M5.5 1C4 5 1 8 1 10a4.5 4 0 0 0 9 0c0-2-3-5-4.5-9z" fill="#F7AB1B"/></svg><span>BOLD &amp;<br>DELICIOUS</span></div>
      <div class="feature"><svg viewBox="0 0 11 14"><path d="M10 1C3 3 1 7 2 13c6-1 8-6 8-12z" fill="#F7AB1B"/></svg><span>NO ARTIFICIAL<br>FLAVORS</span></div>
    </div>
    <div class="lid-net">NET WT 2 OZ</div>
  </div>

  <!-- Sweet Red Sauce lid -->
  <div class="lid lid--sweet">
    <div class="lid-frame"></div>
    <div class="lid-brand"><span class="dot"></span><span class="name">Wokly8</span></div>
    <div class="lid-word word-kicker" style="top:91px">SWEET</div>
    <div class="lid-word word-xl" style="top:128px;font-size:72px">RED</div>
    <div class="lid-word word-sauce" style="top:192px;font-size:36px">SAUCE</div>
    <div class="lid-art" role="img" aria-label="Illustration of a fried chicken drumstick beside a dipping bowl of sauce" style="left:172px;top:80px;width:128px;height:140px;background:linear-gradient(150deg,#f39a3a 0%,#e57a25 55%,#b8421f 100%)"></div>
    <div class="lid-band">⸗ FOR FRIED CHICKEN ⸗</div>
    <div class="lid-features">
      <div class="feature"><svg viewBox="0 0 11 14"><circle cx="6" cy="5" r="4" fill="none" stroke="#F7AB1B" stroke-width="1.4"/><path d="M3 8 1 13" stroke="#F7AB1B" stroke-width="1.4"/></svg><span>SWEET &amp;<br>TANGY FLAVOUR</span></div>
      <div class="feature"><svg viewBox="0 0 11 14"><path d="M5.5 1C4 5 1 8 1 10a4.5 4 0 0 0 9 0c0-2-3-5-4.5-9z" fill="#F7AB1B"/></svg><span>PERFECT<br>DIP &amp; GLAZE</span></div>
      <div class="feature"><svg viewBox="0 0 11 14"><path d="M10 1C3 3 1 7 2 13c6-1 8-6 8-12z" fill="#F7AB1B"/></svg><span>MADE FOR<br>FRIEND CHICKEN</span></div>
    </div>
    <div class="lid-net">NET WT 2 OZ</div>
  </div>

  <!-- Soy Sauce lid -->
  <div class="lid lid--soy">
    <div class="lid-frame"></div>
    <div class="lid-brand"><span class="dot"></span><span class="name">Wokly8</span></div>
    <div class="lid-word word-xl" style="top:93px;font-size:86px">SOY</div>
    <div class="lid-word word-sauce" style="top:174px">SAUCE</div>
    <div class="lid-art" role="img" aria-label="Illustration of a bowl of dark soy sauce with a spoon and soybeans" style="left:180px;top:124px;width:124px;height:104px;background:radial-gradient(circle at 45% 40%,#5a2d1c 0%,#2a150c 45%,#111 100%)"></div>
    <div class="lid-band">⸗ SWEET SOY ⸗</div>
    <div class="lid-features">
      <div class="feature"><svg viewBox="0 0 11 14"><ellipse cx="5.5" cy="7" rx="4" ry="5.5" fill="none" stroke="#DFB272" stroke-width="1.4"/></svg><span>MADE WITH<br>REAL SOYA</span></div>
      <div class="feature"><svg viewBox="0 0 11 14"><path d="M5.5 1C4 5 1 8 1 10a4.5 4 0 0 0 9 0c0-2-3-5-4.5-9z" fill="#DFB272"/></svg><span>RICH &amp;<br>DELICIOUS</span></div>
      <div class="feature"><svg viewBox="0 0 11 14"><path d="M10 1C3 3 1 7 2 13c6-1 8-6 8-12z" fill="#DFB272"/></svg><span>NO ARTIFICIAL<br>FLAVORS</span></div>
    </div>
    <div class="lid-net">NET WT 2 OZ</div>
  </div>

  <!-- Green Sauce lid -->
  <div class="lid lid--green">
    <div class="lid-frame"></div>
    <div class="lid-brand"><span class="dot"></span><span class="name">Wokly8</span></div>
    <div class="lid-word word-xl" style="top:96px;font-size:74px;letter-spacing:0">GREEN</div>
    <div class="lid-word word-sauce" style="top:169px">SAUCE</div>
    <div class="lid-art" role="img" aria-label="Illustration of fresh scallion stalks with sliced green onion rings" style="left:222px;top:82px;width:78px;height:136px;border-radius:30%;background:linear-gradient(180deg,#2f7d2b 0%,#5aa83a 55%,#e8f2d8 100%)"></div>
    <div class="lid-band">⸗ SCALLION OIL ⸗</div>
    <div class="lid-features">
      <div class="feature"><svg viewBox="0 0 11 14"><path d="M4 13V1M7 13 9 2" stroke="#2c5f27" stroke-width="1.4" fill="none"/></svg><span>MADE WITH<br>REAL SCALLION</span></div>
      <div class="feature"><svg viewBox="0 0 11 14"><path d="M5.5 1C4 5 1 8 1 10a4.5 4 0 0 0 9 0c0-2-3-5-4.5-9z" fill="#2c5f27"/></svg><span>FRSH &amp;<br>FLAVORFUL</span></div>
      <div class="feature"><svg viewBox="0 0 11 14"><path d="M10 1C3 3 1 7 2 13c6-1 8-6 8-12z" fill="#2c5f27"/></svg><span>NO ARTIFICIAL<br>FLAVORS</span></div>
    </div>
    <div class="lid-net">NET WT 2 OZ</div>
  </div>

  <p class="review-note">Hello, I created this packaging design in Vectorly Studio. Could you please review the design and let me know if you have any suggestions or changes? I would be happy to make any necessary revisions to ensure it meets your expectations.</p>
  <p class="thanks">Thank you!</p>
  <div class="tool-badges"><i class="tool-a"></i><i class="tool-b"></i></div>

  <div class="footer-bar"></div>
  <div class="footer-frame"></div>
  <div class="footer-item footer-left">
    <svg viewBox="0 0 30 30"><path d="M15 4 9 15l6 9 6-9z" fill="none" stroke="#fff" stroke-width="2"/><circle cx="15" cy="15" r="2" fill="#fff"/><path d="M11 27h8M2 6h26" stroke="#fff" stroke-width="2"/></svg>
    <span>100% Vector Editable</span>
  </div>
  <div class="footer-brand">Wokly8</div>
  <div class="footer-item footer-right">
    <svg viewBox="0 0 30 30"><rect x="8" y="3" width="14" height="8" fill="none" stroke="#fff" stroke-width="2"/><rect x="2" y="11" width="26" height="11" rx="2" fill="#fff"/><rect x="8" y="18" width="14" height="9" fill="#0e0e0e" stroke="#fff" stroke-width="2"/></svg>
    <span>PRINT READY HIGH QUALITY</span>
  </div>
</div>
</body>
</html>
```